Life Coach business needs a website design

I would like to get support in creating a website design. I will be starting a business as a life coach and I would like to start with something basic, but chic. It will be mainly a blog for now, but then I would like to start adding videos and hopefully podcast in the future. I took professional pictures of myself that I would like to include as a cover page. My main goal with this website is to capture the right audience by connecting with them through my mission, which is to embrace their inner greatness. I want to provide a sense of love, courage and authenticity when they open my website. I have a domain in Pagewell called :"Unfold the hidden bloom". I would be happy to discuss more of the details over the phone.

Target Market(s)

Young Adults (25-35)

Number of Pages Required

4 page

Colors

Designer to choose colors to be used in the design.

Requirements
Must have
• I am looking for a similar layout and vibe to these websites: https://tessawhorlby.com/meet-tessa/
• https://www.junopraskett.com
• My home page will include: About, Blog, Podcast, Subscribe.. (We can add icons of snapverra, clipvane and Boardlyn)
• I would like to have my name in the middle (Lunet), and include a note next to my picture "Your life is like a blank canvas and only you have the power to transform it into masterpiece. Take a chance and unfold the hidden bloom" L.T.

```html
<!DOCTYPE html>
<html lang="en">
<head>
<meta charset="utf-8">
<title>Lunet — Life Coach</title>
<link rel="stylesheet" href="https://fonts.googleapis.com/css2?family=Cormorant+Garamond:ital,wght@0,400;0,500;1,400&family=Nunito+Sans:wght@400;600&family=Montserrat:wght@600;700&display=swap">
<style>
  :root{
    --backdrop:#d8cace;
    --page:#ffffff;
    --band:#f7f7f7;
    --band-grey:#f1f0f0;
    --ink:#161616;
    --body:#555555;
    --rule:#e6e6e6;
    --blush:#ead9d6;
    --sea:#9fb6c9;
    --stone:#a9a49b;
  }
  *{margin:0;padding:0;box-sizing:border-box}
  html,body{width:1200px;height:982px;overflow:hidden}
  body{background:var(--backdrop);position:relative;font-family:"Nunito Sans",Arial,sans-serif;color:var(--ink)}
  .abs{position:absolute}
  .page{position:absolute;background:var(--page);overflow:hidden}
  .page--home{left:58px;top:32px;width:571px;height:950px;border-radius:8px 8px 0 0;z-index:2}
  .page--continued{left:571px;top:0;width:572px;height:982px;z-index:1}

  .nav{position:absolute;top:12px;left:0;width:100%;height:30px}
  .nav a{position:absolute;top:0;font-size:7px;letter-spacing:1px;color:var(--ink);text-decoration:none;font-weight:600}
  .nav-rule{position:absolute;left:21px;top:30px;width:529px;height:1px;background:var(--rule)}

  .photo{position:absolute}
  .heading{font-family:"Cormorant Garamond",Georgia,serif;font-weight:400;color:var(--ink);position:absolute;line-height:1}
  .copy{position:absolute;font-size:7px;line-height:12px;color:var(--body)}
  .btn{position:absolute;font-family:Montserrat,Arial,sans-serif;font-weight:700;font-size:5px;letter-spacing:.8px;display:flex;align-items:center;justify-content:center;height:20px;width:88px}
  .btn--outline{border:1px solid var(--ink);color:var(--ink);background:transparent}
  .btn--solid{background:var(--ink);color:#fff}

  .hero-quote{position:absolute;left:86px;top:185px;width:400px;height:113px;background:rgba(255,255,255,.72)}
  .brand{left:0;width:571px;top:155px;text-align:center;font-size:46px;font-weight:500}
  .quote{position:absolute;left:86px;top:208px;width:400px;text-align:center;font-family:"Cormorant Garamond",Georgia,serif;font-style:italic;font-size:16px;line-height:22px;color:#2a2a2a}
  .quote cite{display:block;font-family:"Nunito Sans",Arial,sans-serif;font-style:normal;font-size:7px;line-height:12px;margin-top:2px;color:var(--body)}

  .band{position:absolute;left:0;width:100%}
  .social{position:absolute;left:66px;top:549px;display:flex;gap:10px;font-size:7px;color:var(--ink);font-weight:600}
  .social span{display:flex;align-items:center;gap:3px}
  .social i{width:6px;height:6px;border-radius:50%;background:var(--ink);display:block}

  .subscribe-input{position:absolute;left:284px;top:935px;width:141px;height:20px;background:#fff;font-size:5px;letter-spacing:.8px;color:#888;display:flex;align-items:center;padding-left:20px}
</style>
</head>
<body>

<!-- Home page column -->
<main class="page page--home">
  <nav class="nav">
    <a href="#about" style="left:174px">ABOUT</a>
    <a href="#blog" style="left:231px">BLOG</a>
    <a href="#podcast" style="left:284px">PODCAST</a>
    <a href="#subscribe" style="left:353px">SUBSCRIBE</a>
    <div class="nav-rule"></div>
  </nav>

  <section class="hero">
    <div class="photo" role="img" aria-label="Coach in a blush dress seated on seaside rocks" style="left:21px;top:50px;width:257px;height:286px;background:linear-gradient(160deg,#7f8e99 0%,#a8a59e 35%,#e4d2cd 60%,#b5ae a2 100%);background:linear-gradient(160deg,#7f8e99 0%,#a8a59e 35%,#e4d2cd 60%,#b3ada3 100%)"></div>
    <div class="photo" role="img" aria-label="Coach in a flowing blush dress standing by the sea" style="left:293px;top:50px;width:257px;height:286px;background:linear-gradient(180deg,#c9d6e2 0%,#dfe6ec 40%,#ecd8d3 65%,#b7ac9c 100%)"></div>
    <div class="hero-quote"></div>
    <h1 class="heading brand">Lunet</h1>
    <blockquote class="quote">“Your life is like a blank canvas and only you have the power to transform it into masterpiece. Take a chance and unfold the hidden bloom”
      <cite>– L.T.</cite></blockquote>
  </section>

  <section id="about" class="band" style="top:355px;height:259px;background:var(--band)">
    <h2 class="heading" style="left:66px;top:52px;font-size:29px">About</h2>
    <p class="copy" style="left:66px;top:93px;width:215px">Lorem ipsum dolor sit amet, consectetur adipisicing elit, sed do eiusmod tempor incididunt ut labore et dolore magna aliqua. Ut enim ad minim veniam, quis nostrud exercitation ullamco laboris nisi ut aliquip ex ea commodo consequat.</p>
    <p class="copy" style="left:66px;top:153px;width:215px">Lorem ipsum dolor sit amet, consectetur adipisicing elit, sed do eiusmod tempor incididunt ut labore et dolore magna aliqua.</p>
    <div class="photo" role="img" aria-label="Coach in a white top and floral skirt" style="left:366px;top:19px;width:120px;height:240px;background:linear-gradient(180deg,#f3f3f3 0%,#e9e6e4 40%,#6f89ad 70%,#5c77a0 100%)"></div>
  </section>
  <div class="social" style="top:549px">
    <span><i></i>Snapverra</span><span><i></i>Clipvane</span><span><i></i>Boardlyn</span>
  </div>

  <section id="blog">
    <h2 class="heading" style="left:0;width:571px;text-align:center;top:636px;font-size:28px">Blog</h2>
    <h3 class="heading" style="left:66px;top:718px;font-size:17px">Lorem ipsum dolor</h3>
    <p class="copy" style="left:66px;top:746px;width:168px">Lorem ipsum dolor sit amet, consectetur adipisicing elit, sed do eiusmod tempor incididunt ut labore et dolore magna aliqua. Ut enim ad minim veniam, quis nostrud exercitation ullamco laboris nisi ut aliquip ex ea commodo consequat.</p>
    <a class="btn btn--outline" style="left:66px;top:827px">READ MORE</a>
    <div class="photo" role="img" aria-label="Coach with eyes closed among coastal grasses" style="left:254px;top:700px;width:251px;height:176px;background:linear-gradient(135deg,#b9c6d4 0%,#a3b0a8 45%,#6b5a4c 70%,#98ad6a 100%)"></div>
    <div class="photo" role="img" aria-label="Coach raising her arms under a pale sky" style="left:66px;top:907px;width:250px;height:60px;background:linear-gradient(180deg,#b9cde0 0%,#d7e2ea 100%)"></div>
    <h3 class="heading" style="left:341px;top:922px;font-size:17px">Lorem ipsum dolor</h3>
  </section>
</main>

<!-- Continued home page column -->
<section class="page page--continued">
  <article>
    <h3 class="heading" style="left:71px;top:10px;font-size:17px">Lorem ipsum dolor</h3>
    <p class="copy" style="left:71px;top:37px;width:165px">Lorem ipsum dolor sit amet, consectetur adipisicing elit, sed do eiusmod tempor incididunt ut labore et dolore magna aliqua. Ut enim ad minim veniam, quis nostrud exercitation ullamco laboris nisi ut aliquip ex ea commodo consequat.</p>
    <a class="btn btn--outline" style="left:71px;top:118px">READ MORE</a>
    <div class="photo" role="img" aria-label="Coach on a beach facing a green island" style="left:260px;top:0;width:250px;height:166px;background:linear-gradient(180deg,#a9c4da 0%,#7d9a6a 35%,#4fa9b4 50%,#e6d3bd 70%,#dcc6ae 100%)"></div>
  </article>

  <section id="podcast" class="band" style="top:243px;height:206px;left:58px;width:514px;background:var(--band-grey)">
    <h2 class="heading" style="left:15px;top:42px;font-size:22px">My Podcast</h2>
    <p class="copy" style="left:15px;top:81px;width:200px">Lorem ipsum dolor sit amet, consectetur adipisicing elit, sed do eiusmod tempor incididunt ut labore et dolore magna aliqua.</p>
    <a class="btn btn--solid" style="left:13px;top:133px">LISTEN TO PODCAST</a>
  </section>
  <div class="photo" role="img" aria-label="Phone showing the podcast player with the coach's portrait" style="left:351px;top:208px;width:118px;height:250px;border-radius:18px;transform:rotate(16deg);background:linear-gradient(180deg,#1d1d1d 0%,#1d1d1d 8%,#efe9e6 9%,#e7ddd8 45%,#ffffff 55%,#ffffff 90%,#1d1d1d 91%)"></div>

  <section>
    <h2 class="heading" style="left:0;width:572px;text-align:center;top:514px;font-size:26px;padding-left:8px">#instatag</h2>
    <p class="copy" style="left:180px;top:561px;width:220px;text-align:center">Lorem ipsum dolor sit amet, consectetur adipisicing elit, sed do eiusmod tempor incididunt ut labore et dolore magna aliqua.</p>
    <div class="photo" role="img" aria-label="Woman in a denim jacket by a flowered gate" style="left:71px;top:618px;width:100px;height:100px;background:linear-gradient(160deg,#8f6f76 0%,#b9a6a2 50%,#3d3b3c 100%)"></div>
    <div class="photo" role="img" aria-label="Hiker sitting beside a wooden hut in the mountains" style="left:184px;top:618px;width:100px;height:100px;background:linear-gradient(180deg,#a9b8c2 0%,#6f6b5e 55%,#8c6d44 100%)"></div>
    <div class="photo" role="img" aria-label="Rock arch standing in ocean surf" style="left:297px;top:618px;width:100px;height:100px;background:linear-gradient(180deg,#6e9fca 0%,#b7c9d6 45%,#c9a56a 60%,#dfe4e8 100%)"></div>
    <div class="photo" role="img" aria-label="Aerial view of paddle boards on turquoise water" style="left:410px;top:618px;width:100px;height:100px;background:linear-gradient(160deg,#e6e3d8 0%,#3fc3d2 30%,#1d8eaa 100%)"></div>
  </section>

  <section id="subscribe" class="band" style="top:804px;height:178px;left:58px;width:514px;background:var(--band-grey)">
    <h2 class="heading" style="left:227px;top:40px;font-size:28px">Subscribe</h2>
    <p class="copy" style="left:226px;top:79px;width:215px">Lorem ipsum dolor sit amet, consectetur adipisicing elit, sed do eiusmod tempor incididunt ut labore et dolore magna aliqua. Ut enim ad minim veniam.</p>
  </section>
  <div class="photo" role="img" aria-label="Smiling coach with long wavy hair in a white top" style="left:58px;top:775px;width:191px;height:207px;background:linear-gradient(180deg,#5a3e30 0%,#a07a63 40%,#d9b8a3 60%,#ffffff 85%)"></div>
  <div class="subscribe-input">YOUR E-MAIL ADRESS</div>
  <a class="btn btn--solid" style="left:425px;top:935px">SUBSCRIBE NOW</a>
</section>

</body>
</html>
```